Thistle Root Organic

Please find attached screenshots of a same product as what I'm selling, looking for similar packaging but yet a whole new different design with my own logo rivertiles which is also attached. It will be on white bags with the clear on the bottom center. As far as colors maby green yellow and black or if you have a better idea. Also it needs to be something that looks up to date modern I like when it has that two-tone gloss to it where it goes from darker to lighter.

```html
<!DOCTYPE html>
<html lang="en">
<head>
<meta charset="utf-8">
<title>Thistle Root – Herbs for Wellness Pouch</title>
<link rel="stylesheet" href="https://fonts.googleapis.com/css2?family=Oswald:wght@500;700&family=Playfair+Display:wght@700&family=Montserrat:wght@500&display=swap">
<style>
  :root {
    --backdrop: #6b6b6b;
    --pouch-white: #eeeeee;
    --pouch-edge: #e2e2e2;
    --brand-green: #1f7a3c;
    --deep-green: #0d4a26;
    --band-light: #2a8a3e;
    --band-dark: #0b3f22;
    --herb-light: #7d8f5c;
    --herb-dark: #3f4d2e;
    --white: #ffffff;
  }
  html, body {
    margin: 0;
    padding: 0;
    width: 1200px;
    height: 1118px;
    overflow: hidden;
    background: var(--backdrop);
  }
  .canvas {
    position: relative;
    width: 1200px;
    height: 1118px;
  }
  .pouch-art {
    position: absolute;
    inset: 0;
  }
  .brand-name {
    font-family: "Montserrat", sans-serif;
    font-weight: 500;
    font-size: 30px;
    letter-spacing: 3px;
    fill: var(--brand-green);
  }
  .tagline {
    font-family: "Oswald", sans-serif;
    font-weight: 700;
    font-size: 50px;
    letter-spacing: 1px;
    fill: var(--deep-green);
  }
  .product-name {
    font-family: "Playfair Display", serif;
    font-weight: 700;
    font-size: 54px;
    fill: var(--white);
  }
  .net-weight {
    font-family: "Oswald", sans-serif;
    font-weight: 500;
    font-size: 17px;
    letter-spacing: 0.5px;
    fill: var(--deep-green);
  }
</style>
</head>
<body>
<main class="canvas">
  <svg class="pouch-art" width="1200" height="1118" viewBox="0 0 1200 1118" xmlns="http://www.w3.org/2000/svg">
    <defs>
      <linearGradient id="bandGloss" x1="0" y1="0" x2="1" y2="0.3">
        <stop offset="0" stop-color="var(--band-light)"/>
        <stop offset="0.55" stop-color="#1c6b33"/>
        <stop offset="1" stop-color="var(--band-dark)"/>
      </linearGradient>
      <radialGradient id="herbTone" cx="0.45" cy="0.4" r="0.7">
        <stop offset="0" stop-color="var(--herb-light)"/>
        <stop offset="1" stop-color="var(--herb-dark)"/>
      </radialGradient>
      <clipPath id="pouchShape">
        <rect x="311" y="114" width="570" height="920" rx="24"/>
      </clipPath>
      <path id="taglineArc" d="M 418 760 A 168 168 0 0 1 754 760"/>
    </defs>

    <!-- pouch body -->
    <rect class="pouch-body" x="311" y="114" width="570" height="920" rx="24" fill="var(--pouch-white)"/>

    <g clip-path="url(#pouchShape)">
      <!-- zipper seam -->
      <line x1="311" y1="241" x2="881" y2="241" stroke="var(--pouch-edge)" stroke-width="3"/>

      <!-- divider lines around badge -->
      <line x1="326" y1="477" x2="530" y2="492" stroke="var(--brand-green)" stroke-width="3"/>
      <line x1="650" y1="492" x2="865" y2="480" stroke="var(--brand-green)" stroke-width="3"/>

      <!-- lower two-tone band -->
      <path class="product-band" d="M 311 742 L 881 733 L 881 1034 L 311 1034 Z" fill="url(#bandGloss)"/>
      <line x1="341" y1="726" x2="851" y2="717" stroke="var(--brand-green)" stroke-width="3"/>
      <rect x="311" y="965" width="570" height="69" fill="var(--pouch-white)"/>
    </g>

    <!-- brand mark -->
    <circle cx="600" cy="330" r="27" fill="none" stroke="var(--brand-green)" stroke-width="5"/>
    <text class="brand-name" x="600" y="398" text-anchor="middle">RIVERTILES</text>

    <!-- organic certification badge -->
    <ellipse class="organic-badge" cx="588" cy="492" rx="58" ry="32" fill="var(--brand-green)"/>

    <!-- arched tagline -->
    <text class="tagline" text-anchor="middle">
      <textPath href="#taglineArc" startOffset="50%">HERBS FOR WELLNESS</textPath>
    </text>

    <!-- clear window showing dried herb -->
    <circle cx="585" cy="741" r="146" fill="var(--pouch-white)"/>
    <circle class="product-window" cx="585" cy="741" r="134" fill="url(#herbTone)" role="img" aria-label="Clear window showing dried, cut thistle root herb"/>

    <!-- product name & weight -->
    <text class="product-name" x="588" y="925" text-anchor="middle">Thistle Root</text>
    <text class="net-weight" x="588" y="990" text-anchor="middle">NET WT. 1.27 OZ.(36g)</text>
  </svg>
</main>
</body>
</html>
```